Business Cards that are elegant and wow

I want to create and print business cards that represent my brand and stand out from the rest. We want to ensure they stay in our branding and the integrity is not lost. I am happy to look at different shapes like square etc.

It will be printed on very thick cards and will be stylish .

I want to create and print business cards that represent my brand and stand out from the rest. We want to ensure they stay in ur branding and the integrity is not lost. I am happy to look at different shapes like square etc.

Target Market(s)

real estate professionals

Industry/Entity Type

Real Estate

Contact Information for Business Card

Maren Holt
hello@brightfernrealty.com.au
brightfernrealty.com.au
0487 316 252 (SMS)

Colors

Designer to choose colors to be used in the design.

Requirements
Must have
• My logo
• email
• website
• Name
Nice to have
• I like the idea of printing with foil or spot gloss. You want it to stand out in a sea.
Should not have
• I would like you to stay in my colour themes. Don't change the colour of my logo

```html
<!DOCTYPE html>
<html lang="en">
<head>
<meta charset="utf-8">
<title>Bright Fern Realty – Business Card</title>
<link href="https://fonts.googleapis.com/css2?family=Montserrat:wght@500;600;700&display=swap" rel="stylesheet">
<style>
  :root {
    --brand-blue: #00aeef;
    --brand-pink: #ec0c7e;
    --paper: #ffffff;
    --ink: #474747;
    --backdrop: #b0b0af;
  }
  * { margin: 0; padding: 0; box-sizing: border-box; }
  html, body { width: 1200px; height: 1200px; overflow: hidden; }
  body {
    background: var(--backdrop);
    font-family: "Montserrat", sans-serif;
    position: relative;
  }
  .card {
    position: absolute;
    left: 367px;
    width: 502px;
    height: 295px;
    background: var(--paper);
    overflow: hidden;
  }
  .card--front { top: 231px; }
  .card--back { top: 634px; }

  .edge-strip { position: absolute; right: 0; top: 0; width: 25px; height: 295px; }

  .wordmark { position: absolute; display: flex; align-items: center; }
  .wordmark__dot {
    border: 4px solid var(--brand-blue);
    border-radius: 50%;
    flex: none;
  }
  .wordmark__name {
    color: var(--brand-blue);
    font-weight: 600;
    line-height: 1;
    letter-spacing: 0.02em;
    white-space: nowrap;
  }
  .card--front .wordmark { left: 80px; top: 107px; gap: 16px; }
  .card--front .wordmark__dot { width: 80px; height: 80px; }
  .card--front .wordmark__name { font-size: 32px; }
  .card--front .wordmark__name span { display: block; letter-spacing: 0.42em; margin-top: 6px; }

  .card--back .wordmark { left: 271px; top: 47px; gap: 8px; }
  .card--back .wordmark__dot { width: 38px; height: 38px; border-width: 3px; }
  .card--back .wordmark__name { font-size: 15px; }
  .card--back .wordmark__name span { display: block; letter-spacing: 0.42em; margin-top: 3px; }

  .name-panel {
    position: absolute; left: 0; top: 0;
    width: 243px; height: 295px;
    background: var(--brand-blue);
  }
  .name-panel__name {
    position: absolute; left: 0; right: 0; top: 130px;
    text-align: center;
    color: var(--paper);
    font-weight: 700;
    font-size: 29px;
    letter-spacing: -0.01em;
    white-space: nowrap;
  }
  .social-row {
    position: absolute; left: 60px; top: 235px;
    display: flex; gap: 25px;
  }
  .social-row__item {
    width: 14px; height: 14px;
    border-radius: 50%;
    background: var(--paper);
  }

  .contact-list {
    position: absolute; left: 262px; top: 174px;
    list-style: none;
  }
  .contact-list li {
    display: flex; align-items: center;
    height: 24.5px;
    font-size: 10.5px;
    font-weight: 500;
    color: var(--ink);
    white-space: nowrap;
  }
  .contact-list svg { width: 9px; height: 9px; margin-right: 14px; flex: none; }
</style>
</head>
<body>

<section class="card card--front" aria-label="Card front">
  <div class="wordmark">
    <div class="wordmark__dot"></div>
    <div class="wordmark__name">BRIGHT FERN<span>REALTY</span></div>
  </div>
  <svg class="edge-strip" viewBox="0 0 25 295" aria-hidden="true">
    <polygon points="0,0 25,0 25,105 0,69" fill="var(--brand-pink)"/>
    <polygon points="0,82 25,118 25,295 0,295" fill="var(--brand-blue)"/>
  </svg>
</section>

<section class="card card--back" aria-label="Card back">
  <div class="name-panel">
    <h1 class="name-panel__name">MAREN HOLT</h1>
    <div class="social-row" aria-label="Social profiles">
      <span class="social-row__item"></span>
      <span class="social-row__item"></span>
      <span class="social-row__item"></span>
      <span class="social-row__item"></span>
    </div>
  </div>

  <div class="wordmark">
    <div class="wordmark__dot"></div>
    <div class="wordmark__name">BRIGHT FERN<span>REALTY</span></div>
  </div>

  <ul class="contact-list">
    <li>
      <svg viewBox="0 0 10 10" aria-hidden="true"><path d="M2 0.5 L4 2.5 L3 3.7 Q4.2 6 6.3 7 L7.5 6 L9.5 8 L8 9.5 Q3 9 0.5 2 Z" fill="var(--ink)"/></svg>
      0487 316 252 (SMS)
    </li>
    <li>
      <svg viewBox="0 0 10 10" aria-hidden="true"><rect x="0.5" y="2" width="9" height="6.5" fill="var(--ink)"/><path d="M0.8 2.3 L5 5.6 L9.2 2.3" stroke="var(--paper)" stroke-width="0.9" fill="none"/></svg>
      hello@brightfernrealty.com.au
    </li>
    <li>
      <svg viewBox="0 0 10 10" aria-hidden="true"><g fill="none" stroke="var(--ink)" stroke-width="0.9"><circle cx="5" cy="5" r="4.2"/><ellipse cx="5" cy="5" rx="1.9" ry="4.2"/><path d="M0.8 5 H9.2 M1.5 3 H8.5 M1.5 7 H8.5"/></g></svg>
      brightfernrealty.com.au
    </li>
  </ul>

  <svg class="edge-strip" viewBox="0 0 25 295" aria-hidden="true">
    <polygon points="0,0 25,0 25,105 0,69" fill="var(--brand-pink)"/>
    <polygon points="0,82 25,118 25,295 0,295" fill="var(--brand-blue)"/>
  </svg>
</section>

</body>
</html>
```